**** Business card design for LumaSoft ****

For my ICT company LumaSoft I need I need a business card design.

We design, build and host web-applications and we have our own CMS product.

Some good examples are attached.

The information should be:
Joren Velthuis
Managing director
E: j.velthuis@lumasoft-example.nl
M: +31(0)6 57182604
T: +31(0)40 7214589
W: www.lumasoft-example.nl

Address:
Pieter Dommelenlaan 27
5612 KT Eindhoven

Requirements
Must have
• - Use logo (see attachments)
- Double sided
- Distinctive
Nice to have
• - Place for a statement on the back-side: "Crafted with insight, delivered with care"
- HTML code (or Pagecraft)
- Dark (black or dark-gray) side
- Small simple images for telephone, e-mail en Url.
- QR code (only if not disturbing), not required, just an option

```html
<!DOCTYPE html>
<html lang="en">
<head>
<meta charset="utf-8">
<title>LumaSoft business card</title>
<link rel="stylesheet" href="https://fonts.googleapis.com/css2?family=Exo+2:wght@400;600;700&display=swap">
<style>
  :root {
    --stage-light: #f4f4f5;
    --stage-dark: #c4c5c8;
    --band: #d6d7d9;
    --card-black: #050608;
    --card-navy: #0c1626;
    --card-white: #ffffff;
    --blue-light: #8fd6f1;
    --blue-mid: #35b4e6;
    --logo-silver: #b8c6d2;
    --tagline: #6f98b8;
    --ink: #1a2333;
    --ink-soft: #4a5566;
    --icon-blue: #2a8fc7;
  }
  * { box-sizing: border-box; margin: 0; padding: 0; }
  html, body { width: 1200px; height: 900px; overflow: hidden; }
  body {
    position: relative;
    font-family: "Exo 2", sans-serif;
    background: radial-gradient(ellipse at 50% 45%, var(--stage-light) 0%, #e6e7e8 45%, var(--stage-dark) 100%);
  }
  .backdrop-band {
    position: absolute;
    left: 405px;
    width: 795px;
    background: linear-gradient(90deg, rgba(214,215,217,0) 0%, var(--band) 10%, var(--band) 100%);
    opacity: .8;
  }
  .backdrop-band--top { top: 143px; height: 250px; }
  .backdrop-band--bottom { top: 450px; height: 249px; }

  .card {
    position: absolute;
    width: 405px;
    height: 234px;
    overflow: hidden;
    box-shadow: 0 2px 4px rgba(0,0,0,.18);
  }
  .card--rounded { border-radius: 18px; }
  .card--front-square { left: 167px; top: 159px; }
  .card--front-rounded { left: 630px; top: 159px; }
  .card--back-square { left: 167px; top: 465px; }
  .card--back-rounded { left: 634px; top: 465px; }

  .card-front {
    background: radial-gradient(ellipse at 50% 38%, var(--card-navy) 0%, var(--card-black) 65%);
  }
  .front-logo {
    position: absolute;
    left: 40px;
    top: 58px;
    display: flex;
    align-items: center;
    gap: 22px;
  }
  .logo-dot {
    flex: none;
    width: 64px; height: 64px;
    border-radius: 50%;
    background: var(--blue-mid);
  }
  .logo-name {
    font-weight: 400;
    font-size: 48px;
    letter-spacing: .5px;
    color: var(--logo-silver);
    line-height: 1;
    white-space: nowrap;
  }
  .front-tagline {
    position: absolute;
    left: 0; right: 0;
    top: 181px;
    text-align: center;
    font-size: 13px;
    color: var(--tagline);
  }

  .card-back { background: var(--card-white); }
  .back-curve { position: absolute; left: 0; top: 0; }
  .back-logo {
    position: absolute;
    left: 10px;
    top: 104px;
    display: flex;
    align-items: center;
    gap: 6px;
  }
  .back-logo .logo-dot { width: 20px; height: 20px; }
  .back-logo .logo-name { font-size: 19px; letter-spacing: 0; }

  .holder {
    position: absolute;
    right: 24px;
    top: 30px;
    text-align right;
    text-align: right;
  }
  .holder-name { font-weight: 700; font-size: 20px; color: var(--ink); line-height: 1.1; }
  .holder-role { font-size: 10px; color: var(--ink-soft); }

  .contact-list {
    position: absolute;
    right: 14px;
    top: 136px;
    list-style: none;
  }
  .contact-item {
    display: flex;
    align-items: center;
    justify-content: flex-end;
    gap: 6px;
    font-size: 8px;
    color: var(--ink-soft);
    line-height: 1.15;
    margin-bottom: 3px;
    text-align: right;
    white-space: nowrap;
  }
  .contact-icon { width: 13px; height: 13px; flex: none; }
</style>
</head>
<body>
  <div class="backdrop-band backdrop-band--top" role="img" aria-label="Light grey hatched presentation band"></div>
  <div class="backdrop-band backdrop-band--bottom" role="img" aria-label="Light grey hatched presentation band"></div>

  <section class="card card--front-square card-front">
    <div class="front-logo"><span class="logo-dot"></span><span class="logo-name">LumaSoft</span></div>
    <p class="front-tagline">Crafted with insight, delivered with care</p>
  </section>

  <section class="card card--front-rounded card--rounded card-front">
    <div class="front-logo"><span class="logo-dot"></span><span class="logo-name">LumaSoft</span></div>
    <p class="front-tagline">Crafted with insight, delivered with care</p>
  </section>

  <section class="card card--back-square card-back">
    <svg class="back-curve" width="405" height="234" viewBox="0 0 405 234">
      <path d="M0 0H147Q171 117 147 234H0Z" fill="var(--blue-light)"/>
      <path d="M0 0H127Q157 117 127 234H0Z" fill="var(--blue-mid)"/>
      <path d="M0 0H108Q142 117 108 234H0Z" fill="var(--card-black)"/>
    </svg>
    <div class="back-logo"><span class="logo-dot"></span><span class="logo-name">LumaSoft</span></div>
    <div class="holder">
      <h2 class="holder-name">Joren Velthuis</h2>
      <p class="holder-role">Managing director</p>
    </div>
    <ul class="contact-list">
      <li class="contact-item">www.lumasoft-example.nl
        <svg class="contact-icon" viewBox="0 0 13 13"><circle cx="6.5" cy="6.5" r="5.5" fill="none" stroke="var(--icon-blue)" stroke-width="1.3"/><path d="M1 6.5H12M6.5 1C3.5 4 3.5 9 6.5 12M6.5 1C9.5 4 9.5 9 6.5 12" fill="none" stroke="var(--icon-blue)" stroke-width="1"/></svg></li>
      <li class="contact-item">j.velthuis@lumasoft-example.nl
        <svg class="contact-icon" viewBox="0 0 13 13"><rect x="1" y="3" width="11" height="7.5" fill="none" stroke="var(--icon-blue)" stroke-width="1.3"/><path d="M1 3L6.5 7.5L12 3" fill="none" stroke="var(--icon-blue)" stroke-width="1.1"/></svg></li>
      <li class="contact-item">+31(0)6 57182604
        <svg class="contact-icon" viewBox="0 0 13 13"><rect x="4" y="1" width="5" height="11" rx="1" fill="var(--icon-blue)"/><rect x="5" y="2.5" width="3" height="6" fill="#fff"/></svg></li>
      <li class="contact-item">+31(0)40 7214589
        <svg class="contact-icon" viewBox="0 0 13 13"><path d="M3 1.5L5.2 1.5L6 4.5L4.6 5.6Q5.8 8 7.6 8.6L8.7 7.2L11.5 8V10.4Q11.5 11.5 10.2 11.5Q2 10.8 1.5 2.8Q1.5 1.5 3 1.5Z" fill="var(--icon-blue)"/></svg></li>
      <li class="contact-item">Pieter Dommelenlaan 27<br>5612 KT Eindhoven
        <svg class="contact-icon" viewBox="0 0 13 13"><path d="M6.5 1L12 6H10.5V12H2.5V6H1Z" fill="none" stroke="var(--icon-blue)" stroke-width="1.3"/><rect x="5.3" y="8" width="2.4" height="4" fill="var(--icon-blue)"/></svg></li>
    </ul>
  </section>

  <section class="card card--back-rounded card--rounded card-back">
    <svg class="back-curve" width="405" height="234" viewBox="0 0 405 234">
      <path d="M0 0H147Q171 117 147 234H0Z" fill="var(--blue-light)"/>
      <path d="M0 0H127Q157 117 127 234H0Z" fill="var(--blue-mid)"/>
      <path d="M0 0H108Q142 117 108 234H0Z" fill="var(--card-black)"/>
    </svg>
    <div class="back-logo"><span class="logo-dot"></span><span class="logo-name">LumaSoft</span></div>
    <div class="holder">
      <h2 class="holder-name">Joren Velthuis</h2>
      <p class="holder-role">Managing director</p>
    </div>
    <ul class="contact-list">
      <li class="contact-item">www.lumasoft-example.nl
        <svg class="contact-icon" viewBox="0 0 13 13"><circle cx="6.5" cy="6.5" r="5.5" fill="none" stroke="var(--icon-blue)" stroke-width="1.3"/><path d="M1 6.5H12M6.5 1C3.5 4 3.5 9 6.5 12M6.5 1C9.5 4 9.5 9 6.5 12" fill="none" stroke="var(--icon-blue)" stroke-width="1"/></svg></li>
      <li class="contact-item">j.velthuis@lumasoft-example.nl
        <svg class="contact-icon" viewBox="0 0 13 13"><rect x="1" y="3" width="11" height="7.5" fill="none" stroke="var(--icon-blue)" stroke-width="1.3"/><path d="M1 3L6.5 7.5L12 3" fill="none" stroke="var(--icon-blue)" stroke-width="1.1"/></svg></li>
      <li class="contact-item">+31(0)6 57182604
        <svg class="contact-icon" viewBox="0 0 13 13"><rect x="4" y="1" width="5" height="11" rx="1" fill="var(--icon-blue)"/><rect x="5" y="2.5" width="3" height="6" fill="#fff"/></svg></li>
      <li class="contact-item">+31(0)40 7214589
        <svg class="contact-icon" viewBox="0 0 13 13"><path d="M3 1.5L5.2 1.5L6 4.5L4.6 5.6Q5.8 8 7.6 8.6L8.7 7.2L11.5 8V10.4Q11.5 11.5 10.2 11.5Q2 10.8 1.5 2.8Q1.5 1.5 3 1.5Z" fill="var(--icon-blue)"/></svg></li>
      <li class="contact-item">Pieter Dommelenlaan 27<br>5612 KT Eindhoven
        <svg class="contact-icon" viewBox="0 0 13 13"><path d="M6.5 1L12 6H10.5V12H2.5V6H1Z" fill="none" stroke="var(--icon-blue)" stroke-width="1.3"/><rect x="5.3" y="8" width="2.4" height="4" fill="var(--icon-blue)"/></svg></li>
    </ul>
  </section>
</body>
</html>
```